"Rise. Shift. Thrive." Empowerment Book Cover

Hello, I need a hot, trendy, and contemporary book cover designed for my first book called "Rise. Shift. Thrive. -- 360 Bold Momentum Notes to Guide Anyone to Rise, Shift, and Thrive in Their Career & Daily Dreams."
This is my first book and I am really wanting to launch my brand with it... it would be awesome to match the inside/outside branding of the book. So we can either create the book cover to match the book guts, or update the book guts to match the cover.
Lastly, I just got a professional photoshoot done last week so we can use one of those images, or we can go with a different idea/style for the cover. The body of the book is attached. All questions welcomed, happy designing!
Target Market(s)
Gen Z, Millennials and Gen X.
Industry/Entity Type
Personal Development.
Requirements
Must have
- It must stand out and be different from other typical book covers.
Nice to have
- Success, Inspiration, Motivation, Mindset, Growth.
Should not have
- Clipart, stock art, stock look and feel.

```html
<!DOCTYPE html>
<html lang="en">
<head>
<meta charset="utf-8">
<title>Rise. Shift. Thrive. — Cover Options</title>
<link rel="stylesheet" href="https://fonts.googleapis.com/css2?family=Bevan&family=Abril+Fatface&family=PT+Sans+Narrow&family=Antonio:wght@400&family=Oswald:wght@500&family=Montserrat:wght@400&family=PT+Sans&display=swap">
<style>
  :root {
    --sheet: #e8e8e8;
    --label: #333333;
    --paper: #ffffff;
    --sky: #00a9dd;
    --royal: #0a63d4;
    --navy: #0029a8;
    --teal: #0387ba;
  }
  html, body {
    margin: 0;
    padding: 0;
    width: 884px;
    height: 1200px;
    overflow: hidden;
    background: var(--sheet);
  }
  .sheet {
    position: relative;
    width: 884px;
    height: 1200px;
  }
  .option-number {
    position: absolute;
    font-family: "PT Sans", sans-serif;
    font-size: 34px;
    line-height: 1;
    color: var(--label);
  }
  .cover {
    position: absolute;
    width: 367px;
    height: 546px;
    display: block;
  }
  .cover--one   { left: 50px;  top: 35px;  }
  .cover--two   { left: 466px; top: 35px;  }
  .cover--three { left: 52px;  top: 619px; }
  .cover--four  { left: 468px; top: 619px; }

  .author {
    font-family: "Montserrat", sans-serif;
    font-size: 36px;
    letter-spacing: 9px;
    fill: var(--paper);
  }
  .title-slab    { font-family: "Bevan", serif; font-size: 240px; }
  .title-didone  { font-family: "Abril Fatface", serif; font-size: 250px; }
  .title-narrow  { font-family: "PT Sans Narrow", sans-serif; font-size: 255px; }
  .title-gothic  { font-family: "Antonio", sans-serif; font-size: 255px; }

  .subtitle-slab   { font-family: "Oswald", sans-serif; font-size: 31px; fill: var(--paper); }
  .subtitle-didone { font-family: "Abril Fatface", serif; font-size: 31px; fill: var(--paper); }
  .subtitle-narrow { font-family: "PT Sans Narrow", sans-serif; font-size: 28px; fill: var(--paper); }
  .subtitle-gothic { font-family: "Antonio", sans-serif; font-size: 32px; fill: var(--paper); }
  .panel { fill: var(--paper); }
</style>
</head>
<body>
<main class="sheet">

  <span class="option-number" style="left:22px; top:33px;">1</span>
  <svg class="cover cover--one" viewBox="0 0 685 1020" aria-label="Cover option one">
    <rect width="685" height="1020" fill="var(--sky)"/>
    <text class="author" x="342" y="72" text-anchor="middle">SAMIR HOLDEN</text>
    <rect class="panel" x="0" y="125" width="289" height="222"/>
    <rect class="panel" x="0" y="369" width="567" height="222"/>
    <rect class="panel" x="0" y="618" width="685" height="223"/>
    <g class="title-slab" fill="var(--sky)">
      <text x="8" y="317" textLength="270" lengthAdjust="spacingAndGlyphs">RISE.</text>
      <text x="10" y="561" textLength="470" lengthAdjust="spacingAndGlyphs">SHIFT.</text>
      <text x="10" y="808" textLength="560" lengthAdjust="spacingAndGlyphs">THRIVE.</text>
    </g>
    <g class="subtitle-slab" text-anchor="middle">
      <text x="342" y="950" textLength="560" lengthAdjust="spacingAndGlyphs">360 BOLD MOMENTUM NOTES TO GUIDE ANYONE TO</text>
      <text x="342" y="993" textLength="625" lengthAdjust="spacingAndGlyphs">RISE, SHIFT AND THRIVE IN THEIR CAREER &amp; DAILY DREAMS</text>
    </g>
  </svg>

  <span class="option-number" style="left:438px; top:33px;">2</span>
  <svg class="cover cover--two" viewBox="0 0 685 1020" aria-label="Cover option two">
    <rect width="685" height="1020" fill="var(--royal)"/>
    <text class="author" x="342" y="72" text-anchor="middle">SAMIR HOLDEN</text>
    <rect class="panel" x="0" y="125" width="289" height="222"/>
    <rect class="panel" x="0" y="369" width="567" height="222"/>
    <rect class="panel" x="0" y="618" width="685" height="223"/>
    <g class="title-didone" fill="var(--royal)">
      <text x="16" y="328" textLength="260" lengthAdjust="spacingAndGlyphs">RISE.</text>
      <text x="16" y="572" textLength="470" lengthAdjust="spacingAndGlyphs">SHIFT.</text>
      <text x="16" y="820" textLength="540" lengthAdjust="spacingAndGlyphs">THRIVE.</text>
    </g>
    <g class="subtitle-didone" text-anchor="middle">
      <text x="342" y="936" textLength="530" lengthAdjust="spacingAndGlyphs">360 BOLD MOMENTUM NOTES TO GUIDE ANYONE TO</text>
      <text x="342" y="990" textLength="610" lengthAdjust="spacingAndGlyphs">RISE, SHIFT AND THRIVE IN THEIR CAREER &amp; DAILY DREAMS</text>
    </g>
  </svg>

  <span class="option-number" style="left:24px; top:617px;">3</span>
  <svg class="cover cover--three" viewBox="0 0 685 1020" aria-label="Cover option three">
    <rect width="685" height="1020" fill="var(--navy)"/>
    <g class="subtitle-narrow" text-anchor="middle">
      <text x="342" y="75" textLength="520" lengthAdjust="spacingAndGlyphs">360 BOLD MOMENTUM NOTES TO GUIDE ANYONE TO</text>
      <text x="342" y="108" textLength="610" lengthAdjust="spacingAndGlyphs">RISE, SHIFT AND THRIVE IN THEIR CAREER &amp; DAILY DREAMS</text>
    </g>
    <rect class="panel" x="0" y="173" width="289" height="222"/>
    <rect class="panel" x="0" y="417" width="567" height="222"/>
    <rect class="panel" x="0" y="666" width="685" height="222"/>
    <g class="title-narrow" fill="var(--navy)">
      <text x="16" y="380" textLength="265" lengthAdjust="spacingAndGlyphs">RISE.</text>
      <text x="16" y="625" textLength="470" lengthAdjust="spacingAndGlyphs">SHIFT.</text>
      <text x="16" y="873" textLength="560" lengthAdjust="spacingAndGlyphs">THRIVE.</text>
    </g>
    <text class="author" x="342" y="978" text-anchor="middle">SAMIR HOLDEN</text>
  </svg>

  <span class="option-number" style="left:440px; top:617px;">4</span>
  <svg class="cover cover--four" viewBox="0 0 685 1020" aria-label="Cover option four">
    <rect width="685" height="1020" fill="var(--teal)"/>
    <g class="subtitle-gothic" text-anchor="middle">
      <text x="342" y="68" textLength="460" lengthAdjust="spacingAndGlyphs">360 BOLD MOMENTUM NOTES TO GUIDE ANYONE TO</text>
      <text x="342" y="116" textLength="535" lengthAdjust="spacingAndGlyphs">RISE, SHIFT AND THRIVE IN THEIR CAREER &amp; DAILY DREAMS</text>
    </g>
    <rect class="panel" x="0" y="173" width="289" height="222"/>
    <rect class="panel" x="0" y="417" width="567" height="222"/>
    <rect class="panel" x="0" y="666" width="685" height="222"/>
    <g class="title-gothic" fill="var(--teal)">
      <text x="16" y="380" textLength="215" lengthAdjust="spacingAndGlyphs">RISE.</text>
      <text x="16" y="625" textLength="400" lengthAdjust="spacingAndGlyphs">SHIFT.</text>
      <text x="16" y="872" textLength="460" lengthAdjust="spacingAndGlyphs">THRIVE.</text>
    </g>
    <text class="author" x="342" y="978" text-anchor="middle">SAMIR HOLDEN</text>
  </svg>

</main>
</body>
</html>
```